Gutschein-Design für Apotheken
Zielgruppe
Unsere Familie betreibt 4 Apotheken in Bayern.
Diese haben seit kurzem die Dachmarke und dem CI 'Lerchen-Apotheken', sind aber alle weiter unter eigenem Namen eigenständig.
Unsere Kunden erhalten als Dankeschön für den Besuch einen netten Prämienlerche, der dann gegen schöne Dinge eingetauscht werden kann.
Wir suchen einen neuen Gutschein für unsere Kunden, der in allen Apotheken von uns erworben werden kann und auch überall eingelöst werden kann.
Bisher hatte jede Apotheke einzelne Gutscheine. Die Apotheke Am Lindenhof hat zusätzlich noch einen reinen Kosmetikgutschein, der für Behandlungen etc. ausgegeben wird.
Nun suchen wir einen neuen Gutschein, in dem der Barwert (z.B. 40€) eingetragen wird und der für alles (Arzneimittel, Bonbons etc.) und überall eingelöst werden kann.
Ziel: gemeinsamer Gutschein für Kunden
Format: bevorzugt wie Kosmetikgutschein, gerne aber auch andere Ideen erwünscht (Gutscheinkarte in dem Format, dafür hinten und vorne Info?)
BITTE MODERNES DESIGN, kein klassisches, altbackenes Design von Apotheken (Blümchen etc.)
Inhalt: nicht wirklich viel:
- Gutschein über
- Leerzeichen wo Betrag eingetragen wird
- Gutscheinnummer; Leerzeichen, wo Nummer eingetragen wird
- Datum Unterschrift
- Information, dass dieser Gutschein in allen unseren Apotheken eingelöst werden kann.
- keine Gültigkeit! (Kunden können den Gutschein unendlich lang einlösen bei uns)
- irgend ein netter Spruch? 'Gesundheit ist alles' o.ä 'Gesundheit schenken'... ?!
- evtl. nettes Bild / Gesundheit etc.
- Logos und Adressen von allen 4 Apotheken
- GERNE Lerche mit einbauen (ist unser Wiedererkennungswert! )
(Achtung: 3x Wendtaler Apotheken haben einen technischen Lerche, Apotheke Rodenau hat einen anderen. Ist aber ok so!)
Anbei Beispiele von Flyern, wo wir halbprofessionell schon alle 4 Apotheken mit auf den Flyer tun.
An..
Aufgabenstellung
siehe Anhang

```html
<!DOCTYPE html>
<html lang="de">
<head>
<meta charset="utf-8">
<title>Gutschein – Lerchen-Apotheken</title>
<link href="https://fonts.googleapis.com/css2?family=Oswald:wght@300;400&family=Abel&display=swap" rel="stylesheet">
<style>
  :root{
    --bg:#dde1dd;
    --card:#ffffff;
    --ink:#111111;
    --red:#ff0000;
    --green:#a6ce39;
    --grey:#8a8a8a;
    --line:#e2e2e2;
    --skin:#e9d6cf;
  }
  *{box-sizing:border-box;margin:0;padding:0}
  html,body{width:1200px;height:1136px;overflow:hidden;background:var(--bg)}
  body{position:relative;font-family:"Abel",sans-serif;color:var(--ink)}
  .card{position:absolute;left:66px;width:1067px;background:var(--card);overflow:hidden}
  .card--front{top:65px;height:475px}
  .card--back{top:583px;height:475px}

  /* front */
  .hero-photo{position:absolute;left:0;top:0;width:620px;height:395px;
    background:radial-gradient(ellipse at 35% 40%, var(--skin) 0%, #f3e7e2 45%, #fff 80%),#fff}
  .wave{position:absolute;left:0;top:372px;width:620px;height:40px}
  .amount-circle{position:absolute;left:627px;top:-208px;width:360px;height:360px;border-radius:50%;background:var(--red)}
  .amount{position:absolute;left:742px;top:6px;color:#fff;font-family:"Oswald",sans-serif;font-weight:300;font-size:112px;line-height:1}
  .currency{position:absolute;left:862px;top:20px;color:#fff;font-family:"Oswald",sans-serif;font-weight:300;font-size:38px;line-height:1}
  .front-title{position:absolute;right:34px;top:172px;font-family:"Oswald",sans-serif;font-weight:400;font-size:116px;line-height:1;letter-spacing:-2px}
  .slogan{position:absolute;right:34px;top:302px;font-family:"Oswald",sans-serif;font-weight:300;font-size:44px;line-height:1;color:var(--green)}
  .logo-row{position:absolute;left:0;width:100%;display:flex;justify-content:space-around;align-items:flex-end}
  .card--front .logo-row{top:400px;height:60px}
  .brand{display:flex;align-items:center;gap:8px;font-family:"Abel",sans-serif;font-size:18px;color:var(--ink);text-transform:uppercase;letter-spacing:.5px;white-space:nowrap}
  .brand-dot{width:14px;height:14px;border-radius:50%;background:var(--red);flex:none}

  /* back */
  .back-photo{position:absolute;left:0;top:70px;width:540px;height:270px;opacity:.35;
    background:radial-gradient(ellipse at 45% 20%, #e86a4a 0%, #f2b8a8 18%, transparent 35%),
               linear-gradient(160deg,#d6e6b8 0%,#eef5e0 60%,#fff 100%)}
  .back-title{position:absolute;left:0;width:100%;top:20px;text-align:center;font-family:"Oswald",sans-serif;font-weight:400;font-size:56px;line-height:1}
  .field{position:absolute;background:rgba(255,255,255,.85);border:1px solid var(--line);color:var(--grey);font-family:"Oswald",sans-serif;font-weight:300;display:flex;align-items:center}
  .field--store{left:35px;top:104px;width:997px;height:59px;justify-content:center;font-size:30px}
  .field--number{left:35px;top:178px;width:372px;height:59px;padding-left:5px;font-size:19px}
  .field--date{left:35px;top:254px;width:221px;height:59px;padding-left:5px;font-size:19px}
  .field--sign{left:608px;top:175px;width:424px;height:159px}
  .card--back .logo-row{top:355px;align-items:flex-start}
  .branch{display:flex;flex-direction:column;gap:2px;width:220px}
  .branch .brand{font-size:14px;margin-bottom:3px}
  .branch p{font-size:11px;line-height:1.2;white-space:nowrap}
  .branch p.tiny{font-size:8px}
  .footnote{position:absolute;left:0;width:100%;bottom:4px;text-align:center;font-size:18px;white-space:nowrap}
  .footnote em{font-style:normal;color:var(--red)}
</style>
</head>
<body>

<section class="card card--front">
  <div class="hero-photo" role="img" aria-label="Foto: lächelnde Frau mit Maiglöckchenstrauß und einer kleinen Lerche"></div>
  <svg class="wave" viewBox="0 0 620 40" preserveAspectRatio="none" aria-hidden="true">
    <path d="M0 20 Q20 10 40 20 T80 20 T120 20 T160 20 T200 20 T240 20 T280 20 T320 20 T360 20 T400 20 T440 20 T480 20 T520 20 T560 20 T600 20 T640 20 V40 H0Z" fill="#fff"/>
  </svg>
  <div class="amount-circle"></div>
  <div class="amount">50</div>
  <div class="currency">EUR</div>
  <h1 class="front-title">GUTSCHEIN</h1>
  <p class="slogan">GESUNDHEIT IST ALLES</p>
  <div class="logo-row">
    <div class="brand"><span class="brand-dot"></span>Apotheke Am Lindenhof</div>
    <div class="brand"><span class="brand-dot"></span>Brunnen-Apotheke</div>
    <div class="brand"><span class="brand-dot"></span>Rosen-Apotheke</div>
    <div class="brand"><span class="brand-dot"></span>lindaplus apotheke</div>
  </div>
</section>

<section class="card card--back">
  <div class="back-photo" role="img" aria-label="Blasses Hintergrundfoto: Lerche auf einem grünen Blatt"></div>
  <h2 class="back-title">GUTSCHEIN</h2>
  <div class="field field--store">Rosen Apotheke</div>
  <div class="field field--number">GUTSCHEIN No: 2029340</div>
  <div class="field field--date">DATUM:&nbsp; 10-12-2018</div>
  <div class="field field--sign"></div>

  <div class="logo-row">
    <div class="branch">
      <div class="brand"><span class="brand-dot"></span>Apotheke Am Lindenhof</div>
      <p>Lindenstrasse 6</p>
      <p>TEL: 09471 / 3120-0 &nbsp; FAX: 09471 / 3120-20</p>
      <p class="tiny">lindenhof@lerchen-apotheken.de</p>
    </div>
    <div class="branch">
      <div class="brand"><span class="brand-dot"></span>Brunnen-Apotheke</div>
      <p class="tiny">Am Wehr 4 &nbsp; 92999 Wendtal</p>
      <p class="tiny">Tel: 09471 / 55820 &nbsp; Fax: 09471 / 55821</p>
      <p class="tiny">brunnen@lerchen-apotheken.de</p>
    </div>
    <div class="branch">
      <div class="brand"><span class="brand-dot"></span>Rosen-Apotheke</div>
      <p class="tiny">Kirchgasse 3 &nbsp; Rodenau</p>
      <p class="tiny">Tel: 09663 / 4410-0 &nbsp; Fax: 09663 / 4410-20</p>
      <p class="tiny">rosen@lerchen-apotheken.de</p>
    </div>
    <div class="branch">
      <div class="brand"><span class="brand-dot"></span>lindaplus apotheke</div>
      <p class="tiny">Ziegelstraße 15 &nbsp; 92999 Wendtal</p>
      <p class="tiny">lindaplus@lerchen-apotheken.de</p>
    </div>
  </div>

  <p class="footnote">*Dieser Gutschein <em>in allen unseren Apotheken</em> eingelöst werden kann | <em>Keine Gültigkeit!</em> (Kunden können den Gutschein unendlich lang einlösen bei uns)</p>
</section>

</body>
</html>
```